hello! I need a very simple modern business card for a new venture called The Quiet Harbour Asia. It's the very first Tech-Free retreat in Asia!

The concept is very unique. Basically a group of 12-15 people would go on a 3 to 4 days retreat where no phone or internet is allowed. The first retreat will take place in a beautiful villa in Bali by the sea. It will include yoga, meditation, art & writing workshops, swimming, hiking, cooking, healthy vegetarian meals, etc.

Reason: Thanks for your submissions. I still haven't found exactly what I'm after but the designs that haven't be eliminated are getting close.. Please keep in mind that it should be a simple, modern and upmarket business card. Thanks

Target Market(s)

Both men and women who would like to disconnect from life, computer and phone for 3/4 days. They can be either local or expats but based in Asia (Singapore, Hong Kong).
Client will have to pay for their own flight and then the price is around US$600 for a 3-day retreat including everything (accommodation, food, activities). It means clients already have a good income. They are usually working in marketing, advertising, digital media, public relations.

Industry/Entity Type

Internet

Font styles to use
Other font styles liked:
• anything modern you like

Colors
acd036
9bcb3c
f37022
f68d4d
1b1b1b
333333
acd037

Requirements
Must have
• Name: Rel Vontaine
Position: #screenwanderer
Company: The Quiet Harbour Asia (asia should be smaller than the rest)
- Email button - quietharbourasia@mailnest.example
- Facepage button - www.facepage.example/quietharbourasia
- Ticketloom button - www.quietharbourasia.ticketloom.example
Nice to have
• You can use my logo attached but it's something I designed quickly on Power Point so it would be nice to include your own version.
Should not have
• anything tacky or girly or childish. thanks

```html
<!DOCTYPE html>
<html lang="en">
<head>
<meta charset="utf-8">
<title>Rel Vontaine — The Quiet Harbour Asia</title>
<link rel="stylesheet" href="https://fonts.googleapis.com/css2?family=Ubuntu:wght@300;400;500;700&display=swap">
<style>
  :root {
    --paper: #ffffff;
    --ink: #1b1b1b;
    --ink-soft: #333333;
    --leaf: #9bcb3c;
    --leaf-bright: #acd036;
  }
  * { box-sizing: border-box; margin: 0; padding: 0; }
  html, body { width: 1200px; height: 734px; overflow: hidden; background: var(--paper); }
  .card {
    position: relative;
    width: 1200px;
    height: 734px;
    background: var(--paper);
    font-family: "Ubuntu", sans-serif;
    color: var(--ink);
    overflow: hidden;
  }
  .edge-rule {
    position: absolute; top: 0; left: 1032px;
    width: 6px; height: 734px; background: var(--ink-soft);
  }
  .edge-band {
    position: absolute; top: 0; left: 1048px;
    width: 152px; height: 734px; background: var(--leaf);
  }
  .details {
    position: absolute; top: 220px; left: 0;
    display: grid;
    grid-template-columns: 276px auto;
    column-gap: 14px;
    row-gap: 22px;
    letter-spacing: 0.06em;
    align-items: baseline;
  }
  .label {
    text-align: right;
    font-weight: 300;
    font-size: 35px;
    color: var(--ink-soft);
  }
  .value { font-size: 35px; font-weight: 300; color: var(--ink); }
  .value--name { font-weight: 500; }
  .company { font-weight: 700; color: var(--leaf); letter-spacing: 0.08em; }
  .company-region { font-size: 25px; letter-spacing: 0.08em; }
  .contacts {
    position: absolute; top: 518px; left: 220px;
    list-style: none;
  }
  .contact {
    display: flex; align-items: center;
    height: 48px; margin-bottom: 12px;
    font-size: 32px; font-weight: 300;
    letter-spacing: 0.05em; color: var(--ink);
  }
  .contact svg { width: 50px; height: 44px; margin-right: 20px; flex: none; }
  .contact strong { font-weight: 500; }
  .contact--web { font-weight: 400; }
</style>
</head>
<body>
<main class="card">
  <div class="edge-rule"></div>
  <div class="edge-band"></div>

  <section class="details">
    <span class="label">Name:</span>
    <span class="value value--name">Rel Vontaine</span>

    <span class="label">Position:</span>
    <span class="value">screenwanderer</span>

    <span class="label">Company:</span>
    <span class="value company">The Quiet Harbour <span class="company-region">Asia</span></span>
  </section>

  <ul class="contacts">
    <li class="contact">
      <svg viewBox="0 0 50 44" aria-hidden="true">
        <rect x="3" y="8" width="44" height="30" fill="var(--leaf)"/>
        <polyline points="3,9 25,27 47,9" fill="none" stroke="#fff" stroke-width="3"/>
      </svg>
      quietharbourasia@mailnest.example
    </li>
    <li class="contact">
      <svg viewBox="0 0 50 44" aria-hidden="true">
        <rect x="8" y="2" width="40" height="40" fill="var(--leaf)"/>
      </svg>
      facepage.example/<strong>quietharbourasia</strong>
    </li>
    <li class="contact contact--web">
      <svg viewBox="0 0 50 44" aria-hidden="true">
        <circle cx="27" cy="22" r="18" fill="var(--leaf)"/>
        <g fill="none" stroke="#fff" stroke-width="2.2">
          <circle cx="27" cy="22" r="12"/>
          <ellipse cx="27" cy="22" rx="5" ry="12"/>
          <line x1="15" y1="22" x2="39" y2="22"/>
          <line x1="17" y1="15" x2="37" y2="15"/>
          <line x1="17" y1="29" x2="37" y2="29"/>
        </g>
      </svg>
      www.quietharbourasia.ticketloom.example
    </li>
  </ul>
</main>
</body>
</html>
```